Create a Flyer for switching service Power Falcon based on content

For a promo action for energy supplier switching service. With this flyer we are interested in our customers. The flyer should be in a detailed ppt, ie in an editable format, as we want to be able to include time, date and location specific text later (eg, this promo is for company A / B / C It should also be close to Pflcn's Corporate Design of Energy, accessible at https://powerfalcon-demo.at as, we added logo and designfile to the briefing to help you save time, these are also attached

Target Market(s)

Target Audience are Austrian homeowners or renters, who are in charge of buying electricity and gas. The brochure specifically targets them through their employee represenatives and / or HR departments.

Font styles to use
Sans Serif

Requirements
Must have
• It must be acceptable so we can include specifics for each given company and add contact details landing pages we will create for the specific company representatives.
Nice to have
• Different color schemes, any graphics around saving money,
Should not have
• We do not want to see pictures of real life people included in the design, as we prefer to follow the style of our homepage.

```html
<!DOCTYPE html>
<html lang="de">
<head>
<meta charset="utf-8">
<title>Power Falcon – Betriebsrat Aktion Flyer</title>
<link rel="stylesheet" href="https://fonts.googleapis.com/css2?family=Open+Sans:wght@400;600;700;800&display=swap">
<style>
  :root {
    --backdrop: #e3e3e3;
    --paper: #ffffff;
    --brand-orange: #f29400;
    --band-amber: #f5a623;
    --band-yellow: #f8c72e;
    --band-grey: #8c8c8c;
    --deep-brown: #5a4432;
    --slate: #4b4b4b;
    --ink: #2b2b2b;
    --soft-ink: #6d6d6d;
    --teal: #2ba89b;
    --lime: #c9d43b;
    --cream: #f3e6c8;
    --alert-red: #d8332a;
    --black-box: #1d1d1d;
  }
  * { box-sizing: border-box; margin: 0; padding: 0; }
  html, body {
    width: 1200px; height: 801px; overflow: hidden;
    background: var(--backdrop);
    font-family: "Open Sans", Arial, sans-serif;
    color: var(--ink);
  }
  .flyer {
    position: absolute; left: 330px; top: 18px;
    width: 540px; height: 764px;
    background: var(--paper);
    overflow: hidden;
    box-shadow: 0 6px 18px rgba(0,0,0,.18);
  }
  .flyer-shapes { position: absolute; inset: 0; }
  .abs { position: absolute; }

  .brand { left: 34px; top: 30px; display: flex; align-items: center; gap: 10px; }
  .brand-dot { width: 22px; height: 22px; border-radius: 50%; background: var(--brand-orange); }
  .brand-name { font-weight: 800; font-size: 27px; color: var(--brand-orange); letter-spacing: -.3px; }
  .brand-tag { left: 34px; top: 72px; font-size: 10px; color: var(--soft-ink); }

  .badge {
    right: 34px; top: 24px; width: 100px; height: 100px; border-radius: 50%;
    background: var(--teal); color: #fff; font-size: 10px; font-weight: 600;
    display: flex; align-items: center; justify-content: center; text-align: center; padding: 16px; line-height: 1.3;
  }
  .headline {
    right: 34px; top: 136px; width: 400px; text-align: right;
    color: var(--brand-orange); font-weight: 800; font-size: 16px; line-height: 1.2;
  }
  .headline span { display: block; white-space: nowrap; }
  .headline .caps { text-transform: uppercase; }

  .band-grey-text {
    left: 30px; top: 199px; width: 480px; color: #fff;
    font-size: 9.5px; font-weight: 700; letter-spacing: .4px; text-transform: uppercase; white-space: nowrap;
  }
  .band-amber-title { left: 34px; top: 232px; font-size: 13px; font-weight: 800; color: var(--ink); text-transform: uppercase; }
  .band-amber-text { left: 34px; top: 252px; width: 340px; font-size: 10px; line-height: 1.4; color: var(--ink); }

  .offer { left: 40px; top: 310px; width: 470px; color: var(--band-yellow); font-weight: 700; font-size: 14px; line-height: 1.3; }
  .offer-note { left: 40px; top: 356px; font-size: 9px; color: #e9d9b8; }

  .steps {
    left: 34px; top: 396px; width: 150px; height: 100px;
    background: var(--black-box); color: #fff; font-size: 10px; line-height: 1.55; padding: 10px 12px;
  }
  .steps strong { display: block; color: var(--band-yellow); margin-bottom: 2px; }
  .help {
    left: 34px; top: 504px; width: 150px; height: 44px; background: var(--cream);
    font-size: 10px; padding: 7px 12px; line-height: 1.35;
  }
  .market-text { left: 200px; top: 400px; width: 160px; color: #fff; font-size: 9.5px; line-height: 1.45; }
  .savings {
    left: 372px; top: 390px; width: 138px; height: 118px; border-radius: 22px;
    background: var(--lime); font-size: 11px; font-weight: 700; line-height: 1.35; padding: 16px 14px; color: var(--ink);
  }

  .info-card {
    left: 100px; top: 560px; width: 410px; height: 150px; background: var(--paper);
    border-radius: 14px; padding: 12px 16px; box-shadow: 0 0 0 1px #e6e6e6;
  }
  .info-card h2 { color: var(--alert-red); font-size: 12px; font-weight: 800; margin-bottom: 6px; }
  .info-columns { display: flex; gap: 16px; font-size: 9.5px; line-height: 1.45; color: var(--ink); }
  .info-columns p { flex: 1; }

  .footer-line { left: 34px; top: 728px; width: 472px; font-size: 9.5px; color: var(--brand-orange); font-weight: 600; white-space: nowrap; }
</style>
</head>
<body>
<main class="flyer">
  <svg class="flyer-shapes" viewBox="0 0 540 764" width="540" height="764" aria-hidden="true">
    <path d="M0 188 H540 V226 H0 Z" fill="var(--band-grey)"/>
    <path d="M0 226 H540 V300 H0 Z" fill="var(--band-amber)"/>
    <path d="M380 226 H540 V300 H420 Q380 300 380 262 Z" fill="var(--band-yellow)"/>
    <path d="M20 300 H520 Q540 300 540 320 V360 Q540 382 518 382 H40 Q20 382 20 360 Z" fill="var(--deep-brown)"/>
    <path d="M0 382 H365 Q380 382 380 398 V540 Q380 556 364 556 H0 Z" fill="var(--slate)"/>
    <path d="M0 556 H92 V764 H0 Z" fill="#d9d9d9"/>
    <path d="M92 556 Q60 640 92 720 V556 Z" fill="#c2c2c2"/>
  </svg>

  <div class="abs brand">
    <span class="brand-dot"></span>
    <span class="brand-name">Power Falcon</span>
  </div>
  <p class="abs brand-tag">Dein Wechselservice für Strom und Gas</p>
  <div class="abs badge">Einfach wechseln, jedes Jahr sparen</div>
  <h1 class="abs headline"><span class="caps">Betriebsrat Aktion Zedernthal Bank</span><span>20% Rabatt mit Bonuscode ZBFALCON</span></h1>

  <p class="abs band-grey-text">Mitarbeiter der Zedernthal Bank sparen jetzt mit Power Falcon beim Wechsel</p>
  <h2 class="abs band-amber-title">Wechseln spart immer</h2>
  <p class="abs band-amber-text">Wir vergleichen Strom- und Gasanbieter für dich und wechseln jedes Jahr automatisch zum günstigsten Tarif.</p>

  <p class="abs offer">Mit dem Bonuscode ZBFALCON erhältst du 20% Rabatt auf deine Servicegebühr bei Power Falcon.</p>
  <p class="abs offer-note">Aktion gültig bis 31.12.2016</p>

  <div class="abs steps">
    <strong>So geht's:</strong>
    1. Code eingeben<br>2. Daten ergänzen<br>3. Zurücklehnen
  </div>
  <div class="abs help">Fragen? Wir helfen gerne weiter.</div>
  <p class="abs market-text">Power Falcon beobachtet den Markt laufend und informiert dich, sobald ein besserer Tarif verfügbar ist. Kein Papierkram, keine Unterbrechung der Versorgung.</p>
  <div class="abs savings">Durchschnittlich 300 Euro Ersparnis pro Haushalt im ersten Jahr</div>

  <section class="abs info-card">
    <h2>Warum lohnt sich der Wechsel jetzt?</h2>
    <div class="info-columns">
      <p>Die Energiepreise ändern sich ständig. Wer beim alten Anbieter bleibt, zahlt oft deutlich mehr als nötig. Wir prüfen jedes Jahr alle Tarife für dich.</p>
      <p>Der Wechsel dauert nur wenige Minuten, deine Versorgung läuft ohne Unterbrechung weiter. Alle Formalitäten erledigen wir für dich, sicher und unverbindlich.</p>
    </div>
  </section>

  <p class="abs footer-line">Jetzt anmelden unter https://powerfalcon-demo.at/zedernthal und Bonuscode eingeben</p>
</main>
</body>
</html>
```